Themed design for packaging sleeve and box

1) Gable box 330w x 200d x 160h (image attached for illustration purposes)
2) Sleeve to wrap around our food trays - see image attached

See the images uploaded!!!
This should not be copied, as some are from our competitors and are subject to Copywrite but gives an idea what kind of packaging we would be creating

From all the designs submitted, we will choose one final design and work with this designer to create our full packaging range.....

Target Market(s)

Working adults and health mined people

Font styles to use
Sans Serif

Colors

Designer to choose colors to be used in the design.

Requirements
Must have
• A clean modern look, striking design
Same design in different colours (see the drink bottles idea)
1) meat in shades of red
2) fish in shades of blue
3) vegetable in shades of green
Nice to have
• abstract white against strong colours
use shapes or mosaic or shades of the same colours
Should not have
• overpacked designs with too much information

```html
<!DOCTYPE html>
<html lang="en">
<head>
<meta charset="utf-8">
<title>Evenplate Kosher Meals – Tray Sleeves</title>
<link href="https://fonts.googleapis.com/css2?family=Barlow:wght@300;400;600;700&display=swap" rel="stylesheet">
<style>
  :root {
    --bg-light: #f4f4f4;
    --bg-dark: #c9c9cb;
    --paper: #ffffff;
    --ink: #2b2b2b;
    --meat-deep: #c4122a;
    --meat-mid: #e0344e;
    --meat-soft: #f08a8f;
    --meat-sketch: #e79a86;
    --fish-deep: #1467c0;
    --fish-mid: #3aa0e0;
    --fish-soft: #a9dcf5;
    --fish-sketch: #8fb3df;
    --veg-deep: #2e9b3c;
    --veg-mid: #4fc04f;
    --veg-soft: #b6e6a7;
    --veg-sketch: #a8d9a1;
  }
  * { margin: 0; padding: 0; box-sizing: border-box; }
  html, body { width: 1200px; height: 1035px; overflow: hidden; }
  body {
    position: relative;
    background: linear-gradient(180deg, var(--bg-light) 0%, var(--bg-dark) 100%);
    font-family: "Barlow", Arial, sans-serif;
    color: var(--ink);
  }
  .sleeve {
    position: absolute;
    width: 198px;
    height: 408px;
    background: var(--paper);
    display: flex;
    flex-direction: column;
    align-items: center;
    box-shadow: 0 2px 6px rgba(0,0,0,0.12);
    overflow: hidden;
  }
  .sleeve--meat { left: 286px; top: 242px; --deep: var(--meat-deep); --mid: var(--meat-mid); --soft: var(--meat-soft); --sketch: var(--meat-sketch); }
  .sleeve--fish { left: 716px; top: 104px; --deep: var(--fish-deep); --mid: var(--fish-mid); --soft: var(--fish-soft); --sketch: var(--fish-sketch); }
  .sleeve--veg  { left: 694px; top: 524px; --deep: var(--veg-deep); --mid: var(--veg-mid); --soft: var(--veg-soft); --sketch: var(--veg-sketch); }

  .sleeve__header {
    position: relative;
    width: 100%;
    height: 146px;
    background: linear-gradient(180deg, var(--deep) 0%, var(--mid) 55%, var(--soft) 85%, var(--paper) 100%);
    display: flex;
    flex-direction: column;
    align-items: center;
    padding-top: 44px;
  }
  .brand {
    font-weight: 600;
    font-size: 25px;
    letter-spacing: 1px;
    color: var(--paper);
    line-height: 1;
  }
  .brand__sub {
    margin-top: 8px;
    font-weight: 300;
    font-size: 10px;
    letter-spacing: 7px;
    color: rgba(255,255,255,0.75);
  }
  .claims {
    margin-top: 14px;
    font-weight: 600;
    font-size: 12.5px;
    line-height: 16px;
    text-align: center;
  }
  .claims__item { white-space: nowrap; }
  .tick { width: 8px; height: 8px; margin-right: 2px; vertical-align: 0; }
  .tick path { stroke: var(--ink); stroke-width: 1.4; fill: none; }
  .variant {
    margin-top: 14px;
    width: 90px;
    padding: 3px 0 2px;
    border-top: 1.5px solid var(--deep);
    border-bottom: 1.5px solid var(--deep);
    text-align: center;
    font-size: 20px;
    font-weight: 400;
    letter-spacing: 0.5px;
    color: var(--deep);
    line-height: 22px;
  }
  .variant--wide { width: 92px; }
  .sleeve__art {
    margin-top: auto;
    width: 100%;
    height: 140px;
    background: linear-gradient(180deg, var(--paper) 0%, var(--sketch) 55%, var(--paper) 100%);
    opacity: 0.75;
  }
</style>
</head>
<body>

<section class="sleeve sleeve--meat">
  <div class="sleeve__header" role="img" aria-label="Red triangle mosaic header with white zigzag chevron band">
    <div class="brand">EVENPLATE</div>
    <div class="brand__sub">KOSHER MEALS</div>
  </div>
  <div class="claims">
    <div class="claims__item"><svg class="tick" viewBox="0 0 8 8"><path d="M1 7 L7 1"/></svg>BALANCED <svg class="tick" viewBox="0 0 8 8"><path d="M1 7 L7 1"/></svg>FRESH</div>
    <div class="claims__item"><svg class="tick" viewBox="0 0 8 8"><path d="M1 7 L7 1"/></svg>DELIVERED</div>
  </div>
  <div class="variant">MEET</div>
  <div class="sleeve__art" role="img" aria-label="Red line sketch of steaks, ribs and herbs"></div>
</section>

<section class="sleeve sleeve--fish">
  <div class="sleeve__header" role="img" aria-label="Blue triangle mosaic header with white zigzag chevron band">
    <div class="brand">EVENPLATE</div>
    <div class="brand__sub">KOSHER MEALS</div>
  </div>
  <div class="claims">
    <div class="claims__item"><svg class="tick" viewBox="0 0 8 8"><path d="M1 7 L7 1"/></svg>BALANCED <svg class="tick" viewBox="0 0 8 8"><path d="M1 7 L7 1"/></svg>FRESH</div>
    <div class="claims__item"><svg class="tick" viewBox="0 0 8 8"><path d="M1 7 L7 1"/></svg>DELIVERED</div>
  </div>
  <div class="variant variant--wide">SEE FOOD</div>
  <div class="sleeve__art" role="img" aria-label="Blue line sketch of fish, crab, lobster, shrimp and salmon steaks"></div>
</section>

<section class="sleeve sleeve--veg">
  <div class="sleeve__header" role="img" aria-label="Green triangle mosaic header with white zigzag chevron band">
    <div class="brand">EVENPLATE</div>
    <div class="brand__sub">KOSHER MEALS</div>
  </div>
  <div class="claims">
    <div class="claims__item"><svg class="tick" viewBox="0 0 8 8"><path d="M1 7 L7 1"/></svg>BALANCED <svg class="tick" viewBox="0 0 8 8"><path d="M1 7 L7 1"/></svg>FRESH</div>
    <div class="claims__item"><svg class="tick" viewBox="0 0 8 8"><path d="M1 7 L7 1"/></svg>DELIVERED</div>
  </div>
  <div class="variant variant--wide">SEE FOOD</div>
  <div class="sleeve__art" role="img" aria-label="Green line sketch of peppers, aubergine, beets and leafy vegetables"></div>
</section>

</body>
</html>
```